Stamps and coin dealers need new design for the catalog

We need a new, fresh design for our catalog. We send this catalog every month to our customers. We want a slightly higher quality design for our magazine. The design should of course harmonize with the existing logo. There are pages where we only list products with text and pages with pictures. In addition, we would like to update the cover pages with the payment options, etc. and modernize. These pages should come back a little fresher as well. Title page should be rebuilt. The text modules top left with the year and the title Lindauer Fink and the logo must remain on the page. First page: Here the intro and the table of contents may be renewed. Some space for an advertisement should be created. Last page: Here it is down How to reach us. You are welcome to renew that with a new artwork. The pictures used are relatively old. Of course, the addresses are still correct. In principle, everything should actually be updated and provided with a new design. the logo Briefe Hofer remains the same. It should fit into the new design.
Updates

Ich brauche zusätzliche Tage um durchzusehen

Target Market(s)

Men between 40 and 70 years old collecting stamps and coins

Requirements
Must have
• The design should be a bit simpler and more professional therefore. The standard cover pages as well as the content pages need a new design.
Should not have
• Should not be too playful.

```html
<!DOCTYPE html>
<html lang="de">
<head>
<meta charset="utf-8">
<title>Die Lindauer Fink – Ausgabe 3/2019</title>
<link rel="stylesheet" href="https://fonts.googleapis.com/css2?family=Arimo:wght@400;700&family=Alfa+Slab+One&display=swap">
<style>
:root{
  --bg:#8a9c88;
  --green-deep:#1c5226;
  --green:#2c7434;
  --green-light:#4a9a46;
  --cream:#eef2dc;
  --white:#ffffff;
  --red:#c8161d;
  --yellow:#f4e13a;
  --ink:#1d2a1d;
  --sans:"Arimo", Arial, sans-serif;
  --slab:"Alfa Slab One", Georgia, serif;
}
*{box-sizing:border-box;margin:0;padding:0}
html,body{width:1200px;height:1200px;overflow:hidden}
body{background:var(--bg);font-family:var(--sans);color:var(--ink)}
.spread{position:absolute;left:50px;top:211px;width:1100px;height:778px;display:flex;box-shadow:0 10px 30px rgba(0,0,0,.25)}
.page{position:relative;width:550px;height:778px;overflow:hidden}

/* back cover */
.back{background:radial-gradient(ellipse at 40% 30%,var(--green-light),var(--green) 45%,var(--green-deep))}
.back-head{position:absolute;left:16px;top:22px;right:16px;height:92px;display:flex;gap:10px}
.safe-photo{width:52px;height:62px;margin-top:24px;background:linear-gradient(#d9d4c4,#8e887a);flex:none}
.back-title{font-size:15px;font-weight:700;color:var(--yellow);line-height:1.2}
.back-title u{font-size:17px}
.back-intro{font-size:7.6px;line-height:1.35;color:var(--white);margin-top:5px}
.offers{position:absolute;left:14px;right:14px;top:120px;display:grid;grid-template-columns:repeat(12,1fr);grid-auto-rows:128px;gap:3px}
.offer{background:var(--white);padding:5px;display:flex;flex-direction:column;gap:4px}
.offer.w4{grid-column:span 4}.offer.w8{grid-column:span 8}.offer.w6{grid-column:span 6}.offer.w9{grid-column:span 9}.offer.w3{grid-column:span 3}
.sheets{flex:1;display:flex;gap:3px}
.sheet{flex:1;border:1px solid #cfcfcf}
.offer-text{font-size:6.4px;line-height:1.25;display:flex;justify-content:space-between;gap:6px}
.offer-text b{display:block}
.price{font-weight:700;font-size:8px;white-space:nowrap;align-self:flex-end}
.s-red{background:linear-gradient(#e7a49a,#c9564a)}.s-blue{background:linear-gradient(#9cb5e0,#4566b5)}
.s-green{background:linear-gradient(#c8d7a3,#7f9a55)}.s-teal{background:linear-gradient(#a9cdc6,#4b8f86)}
.s-violet{background:linear-gradient(#c7b3d6,#7d5e9a)}.s-brown{background:linear-gradient(#dbc2a6,#a07550)}
.s-orange{background:linear-gradient(#f6c8a4,#e48a55)}.s-pink{background:linear-gradient(#e6c1c8,#b5737f)}
.s-grey{background:linear-gradient(#d8dbe0,#8b929c)}
.contact-row{position:absolute;left:14px;right:14px;top:648px;height:66px;display:flex;gap:3px}
.album{width:80px;background:linear-gradient(#3d6fb5,#234e8c);flex:none}
.orange-sheets{width:100px;background:linear-gradient(#f6c8a4,#e48a55);flex:none}
.contact-box{flex:1;background:var(--white);font-size:7.5px;line-height:1.35;padding:6px;display:flex;gap:5px;min-width:0}
.contact-box strong{font-size:8.5px;display:block;white-space:nowrap}
.contact-box .nowrap{white-space:nowrap}
.icon{width:18px;height:18px;flex:none}
.reach{position:absolute;left:14px;right:14px;top:718px;height:46px;background:var(--white);padding:6px 10px;display:flex;gap:10px;align-items:center}
.reach h3{font-size:14px;color:var(--green-deep);text-decoration:underline;font-weight:700}
.reach .mark{width:22px;height:22px;background:var(--yellow);border:1px solid var(--ink);flex:none}
.reach p{font-size:9px;line-height:1.25}

/* front cover */
.front{background:linear-gradient(160deg,var(--green),var(--green-deep))}
.front svg.panel{position:absolute;inset:0}
.issue{position:absolute;left:40px;top:22px;color:var(--white);font-weight:700;text-align:center;font-size:11px;line-height:1.2}
.issue .no{font-size:17px}.issue .no small{font-size:12px}
.brand{position:absolute;right:60px;top:14px;background:var(--white);padding:4px 8px;display:flex;align-items:center;gap:6px;font-size:14px;font-weight:700;color:var(--red);text-transform:uppercase;letter-spacing:.5px}
.brand i{width:11px;height:11px;background:var(--red);display:block}
.title-block{position:absolute;left:118px;top:118px;text-align:center;font-weight:700}
.title-block h1{font-size:30px;color:var(--red);line-height:1.1}
.title-block p{font-size:15px;line-height:1.2;color:var(--ink)}
.pig{position:absolute;left:420px;top:78px;width:66px;height:52px;border-radius:10px;background:linear-gradient(#f5c9d3,#e48ea2)}
.promo{position:absolute;left:392px;top:138px;font-family:var(--slab);color:var(--red);font-size:20px;line-height:1.05;text-align:center}
.cover-art{position:absolute;left:70px;top:262px;width:440px;height:300px;border-radius:14px;background:linear-gradient(135deg,#7bbf4d,#3d8a2e 60%,#2f6e26)}
.quality{position:absolute;left:104px;top:300px;font-family:var(--slab);color:var(--red);font-size:21px;transform:rotate(-14deg);transform-origin:left center;z-index:2;white-space:nowrap}
.stamp-red{position:absolute;left:416px;top:268px;width:104px;height:92px;background:linear-gradient(#f2c7c0,#cf6c60);border:4px solid var(--white)}
.stamp-strip{position:absolute;left:470px;top:325px;width:58px;height:250px;background:linear-gradient(#c9b0dd,#8a62a8);border:3px solid var(--white)}
.stamp-view{position:absolute;left:296px;top:456px;width:140px;height:112px;background:linear-gradient(#cfe3ef,#8fa8a0);border:4px solid var(--white)}
.coin-set{position:absolute;left:176px;top:560px;width:180px;height:86px;background:linear-gradient(#8a5a3c,#4a2c1e)}
</style>
</head>
<body>
<main class="spread">

  <section class="page back" aria-label="Rückseite">
    <header class="back-head">
      <div class="safe-photo" role="img" aria-label="Foto eines alten Tresors"></div>
      <div>
        <h2 class="back-title">Aus Uralt - Nachlass: <u>Bogenraritäten für Sammler und Anleger</u></h2>
        <p class="back-intro">Über 60 Jahre hatte ein Fabrikant aus dem Baselbiet seine Briefmarken-Bogen im Safe liegen. Als Anlage erworben und mit Tagesstempel versehen, sind diese Bogen heute sehr selten. Jetzt sind sie in völlig intakter Erhaltung zu günstigen Kursen zu haben. Solange Vorrat!</p>
      </div>
    </header>

    <div class="offers">
      <article class="offer w4">
        <div class="sheets"><div class="sheet s-red" role="img" aria-label="Markenbogen rot"></div><div class="sheet s-blue" role="img" aria-label="Markenbogen blau"></div><div class="sheet s-teal" role="img" aria-label="Markenbogen grün"></div></div>
        <div class="offer-text"><span><b>1960, Werbemarken</b>Originalbogen-Serie mit Tagesstempel, völlig intakt.<b>7300.351.032</b></span><span class="price">98.80 CHF</span></div>
      </article>
      <article class="offer w8">
        <div class="sheets"><div class="sheet s-red" role="img" aria-label="Markenbogen rot"></div><div class="sheet s-blue" role="img" aria-label="Markenbogen blau"></div><div class="sheet s-green" role="img" aria-label="Markenbogen hellgrün"></div></div>
        <div class="offer-text"><span><b>1955, Symbolische Darstellungen</b>Originalbogen-Serie mit Tagesstempel, sehr selten.<b>7300.216.222</b></span><span class="price">195.– CHF</span></div>
      </article>
      <article class="offer w6">
        <div class="sheets"><div class="sheet s-pink" role="img" aria-label="Markenbogen rosa"></div><div class="sheet s-green" role="img" aria-label="Markenbogen grün"></div><div class="sheet s-brown" role="img" aria-label="Markenbogen braun"></div><div class="sheet s-blue" role="img" aria-label="Markenbogen blau"></div></div>
        <div class="offer-text"><span><b>1957, Wappen und Sinnbilder</b>Originalbogen-Serie mit Tagesstempel, völlig intakt.<b>7400.81.092</b></span><span class="price">595.– CHF</span></div>
      </article>
      <article class="offer w6">
        <div class="sheets"><div class="sheet s-pink" role="img" aria-label="Markenbogen rosa"></div><div class="sheet s-green" role="img" aria-label="Markenbogen grün"></div><div class="sheet s-brown" role="img" aria-label="Markenbogen braun"></div><div class="sheet s-violet" role="img" aria-label="Markenbogen violett"></div></div>
        <div class="offer-text"><span><b>1958, Sinnbild, Mineralien</b>Originalbogen-Serie mit Tagesstempel, völlig intakt.<b>7400.86.092</b></span><span class="price">475.– CHF</span></div>
      </article>
      <article class="offer w6">
        <div class="sheets"><div class="sheet s-grey" role="img" aria-label="Markenbogen grau"></div><div class="sheet s-green" role="img" aria-label="Markenbogen grün"></div><div class="sheet s-pink" role="img" aria-label="Markenbogen rosa"></div><div class="sheet s-blue" role="img" aria-label="Markenbogen blau"></div></div>
        <div class="offer-text"><span><b>1960, Mineralien und Versteinerungen</b>Originalbogen-Serie mit Tagesstempel, völlig intakt.<b>7400.96.072</b></span><span class="price">495.– CHF</span></div>
      </article>
      <article class="offer w6">
        <div class="sheets"><div class="sheet s-blue" role="img" aria-label="Markenbogen blau"></div><div class="sheet s-violet" role="img" aria-label="Markenbogen violett"></div><div class="sheet s-brown" role="img" aria-label="Markenbogen braun"></div><div class="sheet s-grey" role="img" aria-label="Markenbogen grau"></div></div>
        <div class="offer-text"><span><b>1961, Sinnbild, Mineralien</b>Originalbogen-Serie mit Tagesstempel, völlig intakt.<b>7400.103.052</b></span><span class="price">235.– CHF</span></div>
      </article>
      <article class="offer w9">
        <div class="sheets"><div class="sheet s-orange" role="img" aria-label="Markenbogen orange"></div><div class="sheet s-green" role="img" aria-label="Markenbogen grün"></div><div class="sheet s-pink" role="img" aria-label="Markenbogen rosa"></div></div>
        <div class="offer-text"><span><b>Bogen-Sortiment</b>Ausgewählte Originalbogen aus dem Nachlass, bestens erhalten.</span><span class="price"></span></div>
      </article>
      <article class="offer w3">
        <div class="offer-text" style="flex:1"><span><b>1950, Technik</b>Markenheftchenbogen mit Tagesstempel, selten angeboten.<b>7330.41.092</b></span></div>
        <div class="offer-text"><span></span><span class="price">59.50 CHF</span></div>
      </article>
    </div>

    <div class="contact-row">
      <div class="album" role="img" aria-label="Blaues Sammelalbum"></div>
      <div class="orange-sheets" role="img" aria-label="Orange Markenbogen"></div>
      <div class="contact-box">
        <svg class="icon" viewBox="0 0 24 24"><circle cx="12" cy="12" r="12" fill="#c8161d"/><path d="M7 8c1-2 3-2 3-2l1 3-1.5 1c.5 1.5 2 3 3.5 3.5L14 12l3 1s0 2-2 3c-4 0-8-4-8-8z" fill="#fff"/></svg>
        <span><strong>071/555 48 20</strong><span class="nowrap">aus dem Ausland:</span><strong>0041/71/555 48 20</strong></span>
      </div>
      <div class="contact-box">
        <svg class="icon" viewBox="0 0 24 24"><rect x="3" y="9" width="18" height="10" rx="2" fill="#2e5fa8"/><rect x="7" y="4" width="10" height="6" fill="#2e5fa8"/></svg>
        <span><strong>071/555 48 21</strong><span class="nowrap">aus dem Ausland:</span><strong>0041/71/555 48 21</strong></span>
      </div>
      <div class="contact-box">
        <span><strong>Internet:</strong>www.briefe-hofer.ch<strong>E-Mail:</strong>bestellungen@<br>briefe-hofer.ch</span>
      </div>
    </div>

    <footer class="reach">
      <h3>So erreichen Sie uns:</h3>
      <span class="mark"></span>
      <p><b>BRIEFE HOFER AG</b><br>Lindenweg 14, 8575 Altdorfen</p>
    </footer>
  </section>

  <section class="page front" aria-label="Titelseite">
    <svg class="panel" viewBox="0 0 550 778" preserveAspectRatio="none" aria-hidden="true">
      <path d="M0 150 C40 80 120 56 200 56 L550 56 L550 560 C420 560 260 610 0 690 Z" fill="var(--cream)"/>
    </svg>
    <div class="issue">97. Jahrgang<br>Mai<br><span class="no">3<small>/2019</small></span></div>
    <div class="brand"><i></i>Briefe Hofer</div>
    <div class="title-block">
      <h1>Die Lindauer Fink</h1>
      <p>Das aktuelle Sammler - Magazin</p>
      <p>Überarbeitete Neuauflage</p>
    </div>
    <div class="pig" role="img" aria-label="Glücksschwein mit Kleeblatt"></div>
    <div class="promo">Saustarke<br>Preise</div>
    <div class="cover-art" role="img" aria-label="Titelillustration: Marienkäfer auf grünen Blättern"></div>
    <div class="quality">Top Qualität ab 25 %</div>
    <div class="stamp-red" role="img" aria-label="Rote gestempelte Briefmarke"></div>
    <div class="stamp-strip" role="img" aria-label="Streifen violetter Briefmarken"></div>
    <div class="stamp-view" role="img" aria-label="Briefmarke mit Bahnhofsgebäude"></div>
    <div class="coin-set" role="img" aria-label="Münzset in Etui"></div>
  </section>

</main>
</body>
</html>
```